Harbourline Sonography Academy (Kestrel Institute of Clinical Scanning) needs an additional web design f

Don't require a redesign of our existing website, I need an additional web design to compliment and feed into our existing web page (kics.edu.au) but establish excellent zintro rankings in it's own right. Web page is to appeal to a specific target market in the allied health industry who wish to learn how to do ultrasound on patients. New website is www. frontlinescanskills.com.au. Our educational institution delivers hands on workshops and seminars on ANYTHING involved with EMERGENCY Ultrasound - intro, advanced, doctors, nurses, etc. Our competitors in this field www.bedsidewavelabs.com.au and www.qpo.edu.au. Looking for a design that will capture the target audience and deliver the message that the courses are delivered by one of the best faculties in Australia. SEO strategies are paramount in that we don't wish to be penalised by Zintro by running a feeder site. Courses are delivered in Sydney and are accredited by an organisation called BRAV.com.au. The courses are listed under 2 qualifications on BRAV website - DLTX and KMRTE. Registrants of our courses are striving to achieve either DLTX - Certificate in Bedside Operator Sonography http://www.brav.com.au/newsite/Files/Documents/Education/DLTX/DLTX_Course_Brochure.pdf OR KMRTE - Certificate in Support Staff Operated Echography http://www.brav.com.au/newsite/Files/Documents/Education/KMRTE/KMRTE_Course_Brochure.pdf.
Website to be lumofon, smartphone and tablet compatible.

Target Market(s)

Emergency Physicians and Emergency nurses/doctors.

Industry/Entity Type

School

Coding

Coded - Design and coding required

Number of Pages Required

2 page

Other font styles liked:
• See website http://www.oakpointdental.com.au/

Colors
86cae6
ec1f27

Requirements
Must have
• Overall professional feel but easy to read and informative.
• Links to our normal website pages www.kics.edu.au
• Ability to rank high.
• Copy of material we deliver here http://www.kics.edu.au/emergency-ultrasound-course-1-3-days/ Click through on relevant dates for more information.
Nice to have
• I like this website - font, feel, layout etc.
• http://www.oakpointdental.com.au/
Should not have
• Information that will lower our zintro rankings knowing it is linked to www.kics.edu.au

```html
<!DOCTYPE html>
<html lang="en">
<head>
<meta charset="utf-8">
<title>Frontline Scan Skills – Emergency Ultrasound Training</title>
<link href="https://fonts.googleapis.com/css2?family=Open+Sans:wght@300;400;600;700&display=swap" rel="stylesheet">
<style>
:root{
  --red:#e3262d;
  --sky:#86cae6;
  --blue:#2a97d4;
  --green:#1f9a5c;
  --ink:#333;
  --muted:#777;
  --line:#e1e1e1;
  --nav:#2b2b2b;
  --band:#262e31;
  --footer:#25292c;
  --footer-base:#1c1f21;
  --white:#fff;
  --date:#2c5aa0;
}
*{box-sizing:border-box;margin:0;padding:0}
html,body{width:712px;height:1200px;overflow:hidden}
body{position:relative;background:var(--white);font-family:"Open Sans",Arial,sans-serif;color:var(--ink);font-size:7px;line-height:1.45}
.abs{position:absolute}
ul{list-style:none}

/* header */
.site-header{left:0;top:0;width:712px;height:52px}
.brand{left:143px;top:11px;font-size:21px;font-weight:400;color:#222;letter-spacing:.3px}
.search{left:433px;top:15px;width:70px;height:10px;border:1px solid #ccc;font-size:5px;color:#aaa;padding-left:3px;line-height:8px}
.social{left:504px;top:15px;display:flex;gap:2px}
.social span{width:9px;height:10px;display:block}
.contact-line{left:470px;top:28px;font-size:5px;color:#777;width:100px;text-align:right;line-height:7px}

/* nav */
.main-nav{left:0;top:52px;width:712px;height:21px;background:var(--nav)}
.main-nav ul{position:absolute;left:148px;top:0;display:flex;gap:12px;height:21px;align-items:center}
.main-nav li{color:#ddd;font-size:6px;display:flex;align-items:center;gap:3px}
.main-nav li i{width:5px;height:5px;background:#bbb;border-radius:1px;display:block}
.main-nav li.active{color:#fff}

/* hero */
.hero{left:0;top:73px;width:712px;height:213px;background:linear-gradient(90deg,#9c87b6 0%,#a796c0 30%,#c7c3cc 55%,#d9d4dc 70%,#9c87b6 100%)}

/* welcome */
.welcome{left:0;top:314px;width:712px;text-align:center}
.welcome h1{font-size:10.5px;font-weight:400;color:#444}
.welcome h1 b{font-weight:700}
.welcome p{font-size:5.5px;color:#777;margin-top:3px}

.card{top:360px;width:115px;height:126px;border:1px solid var(--line);background:#fff;text-align:center}
.card h2{height:14px;font-size:7px;font-weight:400;color:#fff;line-height:14px}
.card .photo{margin:1px 1px 0;height:74px}
.card p{font-size:5px;color:#444;padding:3px 6px 0;line-height:1.5}
.btn-sm{display:inline-block;background:var(--red);color:#fff;font-size:4px;padding:1px 5px;margin-top:3px}

/* events band */
.events{left:0;top:520px;width:712px;height:153px;background:var(--band);color:#fff}
.events .portrait{left:140px;top:2px;width:130px;height:151px;background:linear-gradient(180deg,#3e474b,#d9dde0 60%,#eef0f1)}
.events .pen{left:432px;top:22px}
.events h2{left:300px;top:46px;width:280px;text-align:center;font-size:9px;font-weight:400}
.events h2 b{font-weight:700}
.events .sub{left:300px;top:62px;width:280px;text-align:center;color:var(--sky);font-size:7px}
.events .when{left:300px;top:74px;width:280px;text-align:center;font-size:5px;font-weight:600}
.events .desc{left:298px;top:89px;width:284px;font-size:5.5px;line-height:1.65}
.events .more{left:505px;top:120px;font-size:6px;display:flex;align-items:center;gap:6px}

/* about */
.tabs{left:143px;top:700px;width:204px;height:106px;border:1px solid var(--line);padding:6px 7px}
.tab-row{display:flex;gap:10px;font-size:5.5px;color:#555;border-bottom:1px solid var(--line);padding-bottom:4px}
.tab-row span{display:flex;align-items:center;gap:2px}
.tab-row span.on{color:var(--red)}
.tab-row i{width:4px;height:4px;border:1px solid currentColor;border-radius:50%;display:block}
.tabs p{font-size:5.5px;color:#444;margin-top:5px;line-height:1.55}
.tabs .more{position:absolute;right:8px;bottom:5px;color:var(--red);font-size:6px;display:flex;gap:3px;align-items:center}

.stats{left:364px;top:700px;width:206px}
.stats h3{font-size:6.5px;font-weight:400;color:#444;margin-bottom:6px}
.stat{position:relative;margin-bottom:5px}
.stat span{font-size:5px;color:#444}
.stat em{position:absolute;top:0;font-style:normal;font-size:4px;color:#666}
.bar{height:4px;background:#e6e6e6;margin-top:1px}
.bar b{display:block;height:4px;background:var(--red)}

/* course columns */
.col{top:826px}
.col h4{font-size:6px;font-weight:400;color:var(--red);margin-bottom:5px}
.col-a{left:143px;width:130px;font-size:4.5px;color:#444}
.col-a .org{text-transform:uppercase;line-height:1.5}
.col-a strong{display:block;margin-top:6px;font-size:4.5px}
.col-a li{display:flex;gap:3px;margin-top:4px;align-items:flex-start}
.col-a li i{width:3px;height:3px;border:.6px solid #888;border-radius:50%;display:block;margin-top:1px;flex:none}
.col-a .names{margin-top:5px;line-height:1.9}
.col-b{left:292px;width:130px}
.checks{border:1px solid var(--line);padding:4px 7px}
.checks li{display:flex;gap:4px;align-items:center;font-size:4.5px;color:#444;height:11px}
.checks li i{width:6px;height:6px;border-radius:50%;background:var(--red);display:block;position:relative}
.checks li i:after{content:"";position:absolute;left:2px;top:1px;width:1.5px;height:2.5px;border:solid #fff;border-width:0 .7px .7px 0;transform:rotate(45deg)}
.col-b strong{display:block;font-size:6px;margin-top:7px;line-height:1.4}
.col-b p{font-size:5px;color:#555;margin-top:4px;line-height:1.55}
.col-c{left:440px;width:130px}
.dates{border:1px solid var(--line);padding:6px 8px;font-size:4.3px;color:var(--date);line-height:1.3}
.dates li{margin-bottom:7px}
.dates .note{color:#333;text-transform:uppercase;margin-bottom:7px}

/* cta */
.cta{left:0;top:1042px;width:712px;height:35px;background:var(--band)}
.cta p{position:absolute;left:143px;top:10px;font-size:9px;color:#fff}
.cta .register{position:absolute;left:448px;top:9px;width:120px;height:15px;background:#fff;color:#333;font-size:8px;text-align:center;line-height:15px}
.cta .stripe{position:absolute;left:0;bottom:0;width:712px;height:2px;background:linear-gradient(90deg,var(--band) 0%,var(--red) 20%,var(--red) 45%,var(--band) 50%,var(--sky) 85%,var(--band) 100%)}

/* footer */
.site-footer{left:0;top:1077px;width:712px;height:108px;background:var(--footer);color:#ccc}
.fcol{position:absolute;top:20px;width:130px}
.fcol h5{font-size:6.5px;font-weight:400;color:#aaa;margin-bottom:5px;text-transform:uppercase}
.fcol li{font-size:5.5px;color:#ddd;line-height:1.75}
.fcol p{font-size:5.5px;color:#ddd;line-height:1.75}
.footer-base{left:0;top:1185px;width:712px;height:15px;background:var(--footer-base);color:#888;font-size:5px}
.footer-base span{position:absolute;top:4px}
</style>
</head>
<body>

<header class="abs site-header">
  <div class="abs brand">Logo</div>
  <div class="abs search">Search...</div>
  <div class="abs social" aria-label="Social links">
    <span style="background:#555"></span><span style="background:#2fb0e8"></span><span style="background:#3b5a98"></span><span style="background:#e0467a"></span><span style="background:#2a7bbb"></span><span style="background:#f7a326"></span>
  </div>
  <div class="abs contact-line">☎ 12345678900<br>✉ info@kics.edu.au</div>
</header>

<nav class="abs main-nav">
  <ul>
    <li class="active"><i></i>Home</li>
    <li><i></i>About us</li>
    <li><i></i>Seminars</li>
    <li><i></i>Become a sonographer</li>
    <li><i></i>Consulting</li>
    <li><i></i>Models</li>
    <li><i></i>Information</li>
    <li><i></i>Contact us</li>
  </ul>
</nav>

<div class="abs hero" role="img" aria-label="Smiling sonographer in a white coat beside an instructor and student scanning a patient with an ultrasound machine"></div>

<section class="abs welcome">
  <h1>Welcome to our <b>world</b> Excellence in <b>practical</b> education!</h1>
  <p>The Harbourline Sonography Academy welcomes you to browse the many programs and products available</p>
</section>

<article class="abs card" style="left:144px">
  <h2 style="background:var(--green)">Patient Models</h2>
  <div class="photo" role="img" aria-label="Doctor attending a patient in a hospital bed" style="background:linear-gradient(135deg,#c9dde6,#eef3f5 60%,#b9cdd8)"></div>
  <p>There is a severe shortage of people trained in Medical Ultrasound (Sonography) throughout Australia including Sydney</p>
  <span class="btn-sm">Read More</span>
</article>
<article class="abs card" style="left:300px">
  <h2 style="background:var(--red)">Pregnant Models</h2>
  <div class="photo" role="img" aria-label="Expectant mother with a doctor" style="background:linear-gradient(135deg,#9fc4de,#e8eef3 55%,#b7cfe2)"></div>
  <p>Obstetrics (pregnancy) models in their 1st, 2nd and 3rd Trimesters find it very exciting to come in and have a look</p>
  <span class="btn-sm">Read More</span>
</article>
<article class="abs card" style="left:455px">
  <h2 style="background:var(--blue)">Previous Models' Experiences</h2>
  <div class="photo" role="img" aria-label="Feedback checklist marked excellent" style="background:linear-gradient(135deg,#2d3b2f,#43574a)"></div>
  <p>KICS is seeking past models for its regular training sessions held throughout the year at its campus in Tallow Lane, Merriwood. KICS</p>
  <span class="btn-sm">Read More</span>
</article>

<section class="abs events">
  <div class="abs portrait" role="img" aria-label="Senior doctor with stethoscope, arms crossed"></div>
  <svg class="abs pen" width="16" height="16" viewBox="0 0 16 16" aria-hidden="true"><path d="M3 13 L6 6 L12 2 L14 4 L10 10 Z" fill="none" stroke="#86cae6" stroke-width="1.2"/><path d="M3 13 L8 8" stroke="#86cae6" stroke-width="1"/><path d="M2 15 H8" stroke="#86cae6" stroke-width="1"/></svg>
  <h2 class="abs">New / Upcoming <b>Events</b> and Seminars</h2>
  <div class="abs sub">5day Obstetrics scanning workshop (October)</div>
  <div class="abs when">October 22, 2014 9:00 am - October 26, 2014 4:30 pm</div>
  <p class="abs desc">Course description: Accreditation: BRAV CPD This 5 day 'hands on' introductory course is designed for trainee Sonographers beginning of their ultrasound training in obstetric ultrasound. Curriculum: Physical principles and artifacts</p>
  <div class="abs more">Read more <svg width="10" height="5" viewBox="0 0 10 5"><path d="M0 2.5H9M7 .5L9 2.5 7 4.5" stroke="#fff" fill="none" stroke-width=".8"/></svg></div>
</section>

<section class="abs tabs">
  <div class="tab-row"><span class="on"><i></i>Our Vision</span><span><i></i>Our Mission</span><span><i></i>Our History</span></div>
  <p>KICS develops and produces the highest quality graduates, recruitment solutions and training programs for the medical imaging and allied health workforce in both Australia and overseas.<br>Our vision is to maintain and cement our position as leaders of quality ultra-sound education through continuous improvement and development of the faculty, quality and range of seminars with the highest levels of custom-</p>
  <div class="more">Read More <svg width="10" height="5" viewBox="0 0 10 5"><path d="M0 2.5H9M7 .5L9 2.5 7 4.5" stroke="#e3262d" fill="none" stroke-width=".8"/></svg></div>
</section>

<section class="abs stats">
  <h3>KICS INFORMATION</h3>
  <div class="stat"><span>Seminars and Ultrasound Training on Demand</span><em style="left:80%">80%</em><div class="bar"><b style="width:80%"></b></div></div>
  <div class="stat"><span>Become a Sonographer</span><em style="left:92%">92%</em><div class="bar"><b style="width:92%"></b></div></div>
  <div class="stat"><span>Register to be an KICS Model</span><em style="left:68%">68%</em><div class="bar"><b style="width:68%"></b></div></div>
  <div class="stat"><span>Venue information</span><em style="left:76%">76%</em><div class="bar"><b style="width:76%"></b></div></div>
</section>

<section class="abs col col-a">
  <h4>Emergency Ultrasound Course</h4>
  <div class="org">Kestrel Institute of Clinical Scanning and Scanning Commons</div>
  <strong>FEATURES:</strong>
  <ul>
    <li><i></i>Online Lectures – Prerequisite physics</li>
    <li><i></i>Maximal hands on scanning time</li>
    <li><i></i>Structured Reports</li>
    <li><i></i>Opportunity for Logbook submission</li>
  </ul>
  <strong>DESIGNED AND DELIVERED BY:</strong>
  <ul>
    <li><i></i>Emergency Physicians both post graduate Ultrasound qualifications</li>
    <li><i></i>Sonographers</li>
    <li><i></i>Medical Educationalists</li>
  </ul>
  <div class="names">Dr Miles Varga (Eastbrook Hospital)<br>Dr Tessa Lorne (Greywater General Hospital)<br>Prof Ivan Holcroft (Reedhaven District Hospital)</div>
</section>

<section class="abs col col-b">
  <h4>EMERGENCY ULTRASOUND COURSE – 2 DAYS</h4>
  <ul class="checks">
    <li><i></i>ABDOMINAL AORTIC ANEURYSM (AAA)</li>
    <li><i></i>ULTRASOUND ESSENTIALS</li>
    <li><i></i>E-FAST</li>
    <li><i></i>VASCULAR ACCESS</li>
    <li><i></i>FOREIGN BODIES</li>
    <li><i></i>DVT</li>
  </ul>
  <strong>LIMITED NUMBERS WILL APPLY TO MAXIMIZE HANDS ON LEARNING</strong>
  <p>This course has been accredited by CEPX and BRAV for AAA, E-FAST, Vascular Access, DVT and Basic Cardiac. Please see Scanning Commons for accreditation details<br>Approved for RURAL GP GRANTS FOR EMERGENCY</p>
</section>

<section class="abs col col-c">
  <h4>Book this seminar:</h4>
  <ul class="dates">
    <li>from 8:00 AM on 30/01/2015 3:00 PM 29/01/2015</li>
    <li>from 8:00 AM on 15/05/2015 3:00 PM 14/05/2015</li>
    <li>from 8:00 AM on 04/09/2015 3:00 PM 03/09/2015</li>
    <li class="note">Emergency Ultrasound Course DAY (AM) no option 1 -<br><br>(Basic Echocardiography in Life Support (BELS)</li>
    <li>from 8:00 AM on 31/01/2015 3:50 PM 31/01/2015</li>
    <li>from 8:00 AM on 16/05/2015 3:50 PM 16/05/2015</li>
    <li>from 8:00 AM on 05/09/2015 3:50 PM 05/09/2015</li>
  </ul>
</section>

<section class="abs cta">
  <p>Interested? Find a Seminar or Course and register with Ultrasound</p>
  <div class="register">REGISTER ONLINE</div>
  <div class="stripe"></div>
</section>

<footer class="abs site-footer">
  <div class="fcol" style="left:143px">
    <h5>Sonography</h5>
    <ul><li>GPMU Program Overview</li><li>ISP Program Overview</li><li>ISP Trainer Testimonials</li><li>Meet some past students</li></ul>
  </div>
  <div class="fcol" style="left:293px">
    <h5>Information</h5>
    <ul><li>Accommodation</li><li>Local Information</li><li>Useful Links</li><li>Venue information</li></ul>
  </div>
  <div class="fcol" style="left:440px">
    <h5>Contact Information</h5>
    <p>Ut pri noster corpora an eripuit feugiat id vel nosum libris inermis</p>
    <p>Contact Us</p>
    <h5 style="margin-top:4px">Student Online Resource</h5>
  </div>
</footer>
<div class="abs footer-base">
  <span style="left:143px">Copyright 2014, Northvale Studio. All rights reserved.</span>
  <span style="left:463px">Home</span>
  <span style="left:502px">About Us</span>
  <span style="left:547px">Seminars</span>
</div>

</body>
</html>
```